Belle Rive Weddings and Events

I am a small boutique wedding coordinator, stylist and bridal consultant/coach/assistant. I am based in Brisbane, Australia and my business is geared towards mid range- high end budget bridal couples.
I am after some business cards that are double sided, with the logo on one side and all other information on the other side, including the business tagline of design, create, celebrate. The look of the card needs to be clean and crisp, with white and the tones of grey of the logo.The final design needs to convey sophistication and poise. Perhaps the logo and tagline could be done in a metallic silver with the rest of the text in the shades of grey from the style guide attached below.
Title- Mira Tolvarenko - Director / Events Manager and Stylist
Address - 218 Halbrook Terrace, Wexley Vale, QLD, 4127
Phone- 07 3894 2167
Mobile- 0438 725 519
Email- Mira@bellerivecelebra.com.au
Website- www.bellerivecelebra.com.au

```html
<!DOCTYPE html>
<html lang="en">
<head>
<meta charset="utf-8">
<title>Belle Rive Weddings and Events – Business Card</title>
<link rel="stylesheet" href="https://fonts.googleapis.com/css2?family=Didact+Gothic&family=Poiret+One&display=swap">
<style>
  :root {
    --backdrop: #e9e7e4;
    --card-dark: #152020;
    --card-dark-deep: #0f1717;
    --card-light: #ffffff;
    --silver: #d9dcdc;
    --silver-soft: #9ea4a4;
    --ink: #2b2b2b;
    --ink-soft: #4a4a4a;
    --ornament: #c9c9c9;
  }
  * { box-sizing: border-box; margin: 0; padding: 0; }
  html, body { width: 1200px; height: 800px; overflow: hidden; }
  body {
    background: var(--backdrop);
    display: flex;
    align-items: center;
    justify-content: center;
    gap: 70px;
    font-family: "Didact Gothic", "Century Gothic", sans-serif;
  }

  /* ---------- Logo side ---------- */
  .card-front {
    position: relative;
    width: 340px;
    height: 595px;
    background: var(--card-dark);
    box-shadow: 0 10px 30px rgba(0,0,0,.18);
    overflow: hidden;
    display: flex;
    align-items: center;
    justify-content: center;
  }
  .card-front-shade {
    position: absolute;
    inset: 0;
    background: linear-gradient(135deg, #1d2a2a 0%, #1d2a2a 48%, var(--card-dark-deep) 48%, var(--card-dark-deep) 100%);
    opacity: .9;
  }
  .brand {
    position: relative;
    display: flex;
    flex-direction: column;
    align-items: center;
    color: var(--silver);
  }
  .brand-lockup {
    display: flex;
    align-items: center;
    gap: 14px;
  }
  .brand-mark {
    width: 16px;
    height: 16px;
    border: 1.5px solid var(--silver);
    border-radius: 50%;
    flex: none;
  }
  .brand-name {
    font-family: "Poiret One", "Didact Gothic", sans-serif;
    font-size: 54px;
    line-height: 1;
    letter-spacing: 1px;
  }
  .brand-sub {
    margin-top: 14px;
    font-size: 16px;
    letter-spacing: 1.5px;
  }
  .brand-divider {
    width: 150px;
    height: 1px;
    background: var(--silver-soft);
    margin: 26px 0 16px;
  }
  .brand-tagline {
    font-size: 13px;
    letter-spacing: 3px;
    text-transform: uppercase;
    color: var(--silver-soft);
  }

  /* ---------- Info side ---------- */
  .card-back {
    position: relative;
    width: 595px;
    height: 340px;
    background: var(--card-light);
    box-shadow: 0 10px 30px rgba(0,0,0,.18);
    color: var(--ink);
  }
  .flourish {
    position: absolute;
    left: 24px;
    top: 26px;
    width: 120px;
    height: 170px;
    border-radius: 60% 40% 45% 55% / 50% 45% 55% 50%;
    background: radial-gradient(ellipse at 35% 45%, #e2e2e2 0%, #f3f3f3 50%, rgba(255,255,255,0) 72%);
  }
  .frame-rule {
    position: absolute;
    background: var(--ink);
  }
  .frame-rule--top { right: 48px; top: 38px; width: 250px; height: 3px; }
  .frame-rule--outer { right: 40px; top: 38px; width: 3px; height: 245px; }
  .frame-rule--inner { right: 48px; top: 48px; width: 1.5px; height: 225px; }
  .contact {
    position: absolute;
    right: 64px;
    top: 56px;
    text-align: right;
  }
  .contact-name {
    font-family: "Poiret One", "Didact Gothic", sans-serif;
    font-weight: 400;
    font-size: 36px;
    color: var(--ink);
    line-height: 1.1;
  }
  .contact-title {
    font-size: 14px;
    color: var(--ink-soft);
    margin-top: 4px;
    margin-bottom: 22px;
  }
  .contact-list { list-style: none; }
  .contact-list li {
    display: flex;
    align-items: center;
    justify-content: flex-end;
    gap: 8px;
    font-size: 14.5px;
    line-height: 21px;
    color: var(--ink-soft);
  }
  .contact-icon {
    width: 14px;
    height: 14px;
    background: var(--ink);
    border-radius: 2px;
    display: inline-flex;
    align-items: center;
    justify-content: center;
  }
  .contact-address {
    position: absolute;
    right: 64px;
    bottom: 30px;
    font-size: 14.5px;
    letter-spacing: .5px;
    color: var(--ink-soft);
    text-transform: uppercase;
  }
</style>
</head>
<body>

  <section class="card-front" aria-label="Card logo side">
    <div class="card-front-shade"></div>
    <div class="brand">
      <div class="brand-lockup">
        <span class="brand-mark"></span>
        <span class="brand-name">Belle Rive</span>
      </div>
      <span class="brand-sub">Weddings &amp; Events</span>
      <span class="brand-divider"></span>
      <span class="brand-tagline">design · create · celebrate</span>
    </div>
  </section>

  <section class="card-back" aria-label="Card contact side">
    <div class="flourish" role="img" aria-label="Grey swirl flourish ornament"></div>
    <span class="frame-rule frame-rule--top"></span>
    <span class="frame-rule frame-rule--outer"></span>
    <span class="frame-rule frame-rule--inner"></span>

    <div class="contact">
      <h1 class="contact-name">Mira Tolvarenko</h1>
      <p class="contact-title">Director | Events Manager and Stylist</p>
      <ul class="contact-list">
        <li>07 3894 2167
          <span class="contact-icon"><svg width="9" height="9" viewBox="0 0 10 10"><path d="M2 1l2 2-1 1.5c.7 1.3 1.2 1.8 2.5 2.5L7 6l2 2-1.5 1.5C4 9 1 6 .5 2.5z" fill="#fff"/></svg></span>
        </li>
        <li>0438 725 519
          <span class="contact-icon"><svg width="9" height="9" viewBox="0 0 10 10"><rect x="3" y="1" width="4" height="8" rx="1" fill="none" stroke="#fff" stroke-width="1.2"/></svg></span>
        </li>
        <li>Mira@bellerivecelebra.com.au
          <span class="contact-icon"><svg width="9" height="9" viewBox="0 0 10 10"><rect x="1" y="2.5" width="8" height="5" fill="none" stroke="#fff" stroke-width="1"/><path d="M1 2.5l4 3 4-3" fill="none" stroke="#fff" stroke-width="1"/></svg></span>
        </li>
        <li>www.bellerivecelebra.com.au
          <span class="contact-icon"><svg width="9" height="9" viewBox="0 0 10 10"><circle cx="5" cy="5" r="3.8" fill="none" stroke="#fff" stroke-width="1"/><path d="M1.2 5h7.6M5 1.2v7.6" stroke="#fff" stroke-width=".8"/></svg></span>
        </li>
      </ul>
    </div>

    <p class="contact-address">218 Halbrook Terrace, Wexley Vale, QLD, 4127</p>
  </section>

</body>
</html>
```